Business Card Design

After a corporate career in the finance sector I am now operating on my own as a consultant. I require a simple design, and want a strong card which is targeted at a conservative audience.

Target Market(s)

highly educated senior management, directors of companies, finance sector

Industry/Entity Type

Conservative

Contact Information for Business Card

Ruth Danver
Consultant
Mobile: 0417 862 450
Email: ruth.danv@mailcove.net

Requirements
Should not have
• I don't want the colours green/yellow/brown

```html
<!DOCTYPE html>
<html lang="en">
<head>
<meta charset="utf-8">
<title>Ruth Danver – Consultant</title>
<link rel="stylesheet" href="https://fonts.googleapis.com/css2?family=Play:wght@400;700&display=swap">
<style>
  :root {
    --charcoal: #333233;
    --paper: #ffffff;
    --teal: #128a95;
    --ink: #333233;
  }
  html, body {
    margin: 0;
    padding: 0;
    overflow: hidden;
    background: var(--paper);
  }
  .card {
    position: relative;
    width: 1200px;
    height: 741px;
    overflow: hidden;
    background: var(--paper);
    font-family: "Play", sans-serif;
    color: var(--ink);
  }
  .card__shapes {
    position: absolute;
    inset: 0;
  }
  .shape-dark { fill: var(--charcoal); }
  .shape-band { fill: var(--teal); }

  .identity {
    position: absolute;
    left: 0;
    top: 190px;
    width: 1210px;
    text-align: center;
  }
  .identity__name {
    margin: 0;
    font-size: 112px;
    font-weight: 400;
    line-height: 1;
    letter-spacing: 1px;
    word-spacing: 18px;
    text-transform: uppercase;
    text-shadow: 3px 6px 6px rgba(0, 0, 0, 0.28);
  }
  .identity__role {
    margin: 8px 0 0;
    font-size: 34px;
    font-weight: 400;
    letter-spacing: 6px;
    text-transform: uppercase;
  }

  .contact {
    position: absolute;
    left: 708px;
    top: 563px;
    margin: 0;
    padding: 0;
    list-style: none;
  }
  .contact__item {
    display: flex;
    align-items: center;
    height: 44px;
    font-size: 35px;
    text-shadow: 1px 2px 3px rgba(0, 0, 0, 0.3);
  }
  .contact__icon {
    width: 32px;
    height: 32px;
    margin-right: 28px;
    fill: var(--ink);
    stroke: var(--ink);
  }
</style>
</head>
<body>
<main class="card">
  <svg class="card__shapes" width="1200" height="741" viewBox="0 0 1200 741" aria-hidden="true">
    <polygon class="shape-dark" points="0,0 738,0 0,191"/>
    <polygon class="shape-dark" points="1200,360 313,741 1200,741"/>
    <rect class="shape-band" x="0" y="545" width="1200" height="112"/>
  </svg>

  <header class="identity">
    <h1 class="identity__name">Ruth Danver</h1>
    <p class="identity__role">Consultant</p>
  </header>

  <ul class="contact">
    <li class="contact__item">
      <svg class="contact__icon" viewBox="0 0 32 32" aria-hidden="true">
        <path stroke="none" d="M4 12c0-4 5-6 12-6s12 2 12 6v2h-6v-3h-12v3H4z"/>
        <path stroke="none" d="M8 15h16l3 11H5z"/>
        <g fill="var(--teal)" stroke="none">
          <rect x="12" y="18" width="2" height="2"/><rect x="15" y="18" width="2" height="2"/><rect x="18" y="18" width="2" height="2"/>
          <rect x="12" y="21" width="2" height="2"/><rect x="15" y="21" width="2" height="2"/><rect x="18" y="21" width="2" height="2"/>
        </g>
      </svg>
      <span class="contact__text">0417 862 450</span>
    </li>
    <li class="contact__item">
      <svg class="contact__icon" viewBox="0 0 32 32" aria-hidden="true">
        <g fill="none" stroke-width="2">
          <circle cx="16" cy="16" r="12"/>
          <ellipse cx="16" cy="16" rx="5" ry="12"/>
          <line x1="4" y1="16" x2="28" y2="16"/>
          <path d="M6 10h20M6 22h20"/>
        </g>
      </svg>
      <span class="contact__text">ruth.danv@mailcove.net</span>
    </li>
  </ul>
</main>
</body>
</html>
```